Pelbrook Business Cards

Create new business cards with the details below.

Aaron Velst
Director

MB: +61 412 563 904
PH: 1300 417 639
Email: aaron.velst@pelbrook.com.au
Address: 27C Marlow Parade, Kelverton VIC 3472 Australia
Website: www.pelbrook.com.au

Target Market(s)

Other business

Industry/Entity Type

Business

Requirements
Must have
• must be clean looking

```html
<!DOCTYPE html>
<html lang="en">
<head>
<meta charset="utf-8">
<title>Pelbrook Business Card</title>
<link href="https://fonts.googleapis.com/css2?family=Roboto+Condensed:wght@300;400;700&display=swap" rel="stylesheet">
<style>
  :root {
    --backdrop: #2a2a2a;
    --card: #ffffff;
    --charcoal: #3b3b3b;
    --slate: #5c5c5c;
    --mist: #d9d9d9;
    --lime: #9ccc3c;
    --lime-dark: #7fae25;
    --ink: #2e2e2e;
  }
  * { margin: 0; padding: 0; box-sizing: border-box; }
  html, body { width: 1200px; height: 959px; overflow: hidden; }
  body {
    background: var(--backdrop);
    font-family: "Roboto Condensed", Arial, sans-serif;
    position: relative;
  }
  .card {
    position: absolute;
    left: 150px; top: 215px;
    width: 900px; height: 530px;
    background: var(--card);
    overflow: hidden;
  }
  .top-band { position: absolute; left: 0; top: 60px; }
  .brand {
    position: absolute; left: 560px; top: 140px;
    display: flex; align-items: center; gap: 16px;
  }
  .brand-square { width: 40px; height: 40px; background: var(--lime); }
  .brand-name {
    font-weight: 700; font-size: 52px; letter-spacing: 1px;
    color: var(--charcoal); text-transform: uppercase;
    white-space: nowrap;
  }
  .identity {
    position: absolute; left: 60px; top: 272px;
    font-size: 30px; text-transform: uppercase; letter-spacing: 1px;
    white-space: nowrap;
  }
  .identity .name { color: var(--charcoal); font-weight: 700; }
  .identity .divider { color: var(--mist); margin: 0 10px; font-weight: 300; }
  .identity .role { color: var(--lime-dark); font-weight: 400; }
  .contact-band {
    position: absolute; left: 0; top: 330px; width: 900px; height: 56px;
    background: var(--mist);
    display: flex; align-items: center;
  }
  .contact-band .email {
    padding-left: 60px; font-size: 21px; color: var(--ink); flex: 1;
    white-space: nowrap;
  }
  .contact-band .lines {
    height: 56px; background: var(--charcoal);
    display: flex; align-items: center; gap: 26px;
    padding: 0 40px 0 30px; color: #fff; font-size: 19px;
    white-space: nowrap;
  }
  .item { display: flex; align-items: center; gap: 8px; }
  .item svg { width: 18px; height: 18px; fill: var(--lime); }
  .web-row {
    position: absolute; right: 40px; top: 290px;
    font-size: 19px; color: var(--slate);
    white-space: nowrap;
  }
  .address-band {
    position: absolute; left: 0; top: 386px; width: 900px; height: 144px;
    background: linear-gradient(180deg, var(--lime) 0%, var(--lime-dark) 100%);
  }
  .address-band .address {
    position: absolute; left: 60px; top: 34px;
    font-size: 22px; color: var(--ink);
    white-space: nowrap;
  }
</style>
</head>
<body>
  <div class="card">
    <svg class="top-band" width="560" height="60" viewBox="0 0 560 60" aria-hidden="true">
      <defs>
        <linearGradient id="bandShade" x1="0" x2="1">
          <stop offset="0" stop-color="#6a6a6a"/>
          <stop offset="1" stop-color="#3b3b3b"/>
        </linearGradient>
      </defs>
      <polygon points="0,0 560,0 520,60 0,60" fill="url(#bandShade)"/>
    </svg>

    <div class="brand">
      <span class="brand-square"></span>
      <span class="brand-name">Pelbrook</span>
    </div>

    <div class="web-row item">
      <svg viewBox="0 0 20 20"><circle cx="10" cy="10" r="9"/></svg>
      www.pelbrook.com.au
    </div>

    <div class="identity">
      <span class="name">Aaron Velst</span><span class="divider">|</span><span class="role">Director</span>
    </div>

    <div class="contact-band">
      <span class="email">aaron.velst@pelbrook.com.au</span>
      <div class="lines">
        <span class="item">
          <svg viewBox="0 0 20 20"><path d="M4 2h4l2 5-3 2a11 11 0 0 0 4 4l2-3 5 2v4a2 2 0 0 1-2 2A16 16 0 0 1 2 4a2 2 0 0 1 2-2z"/></svg>
          1300 417 639
        </span>
        <span class="item">
          <svg viewBox="0 0 20 20"><rect x="5" y="1" width="10" height="18" rx="2"/></svg>
          +61 412 563 904
        </span>
      </div>
    </div>

    <div class="address-band">
      <span class="address">27C Marlow Parade, Kelverton VIC 3472 | Australia</span>
    </div>
  </div>
</body>
</html>
```